Business Cards Brightvow Weddings

I have a new webpage address and would like to update my business cards with Facebook and Instagram links as well. I need assistance with designing it. I have attached an old business card.

Target Market(s)

Potential couples wanting to get married and vendors who work with weddings

Industry/Entity Type

Wedding

Contact Information for Business Card

Name of Company (Brightvow Weddings), Kay Whitfield, Phone number (480-555-0173), Webpage: www.brightvowweddings2go.example, Facebook Link: Brightvow Weddings, Instagram Link: BrightvowWeddings2go

Colors
0094D4
00A9DD
6FCCEA
C7EBF8
E9F6FB
00AB8E
00BBA5
67D7C9
C6EFE9
E9F9F6

Requirements
Nice to have
• Florals with teal on back of card. Not sure what needs to be on front and what on back
Should not have
• Definitive man/woman couple

```html
<!DOCTYPE html>
<html lang="en">
<head>
<meta charset="utf-8">
<title>Brightvow Weddings – Business Cards</title>
<link href="https://fonts.googleapis.com/css2?family=Libre+Baskerville:wght@400;700&display=swap" rel="stylesheet">
<style>
  :root {
    --backdrop: #1e1e22;
    --card: #e8f6f4;
    --ink: #111111;
    --petal-pink: #ee7fa6;
    --petal-coral: #f5a27a;
    --leaf-teal: #6fcfe0;
    --leaf-green: #a9cf6a;
    --shadow: rgba(0, 0, 0, 0.45);
  }
  * { margin: 0; padding: 0; box-sizing: border-box; }
  html, body {
    width: 1200px;
    height: 800px;
    overflow: hidden;
    background: var(--backdrop);
    font-family: "Libre Baskerville", Georgia, serif;
    color: var(--ink);
  }
  .sheet {
    width: 1200px;
    height: 800px;
    display: flex;
    align-items: center;
    justify-content: center;
    gap: 40px;
  }
  .card {
    position: relative;
    width: 540px;
    height: 309px;
    background: var(--card);
    border-radius: 22px;
    box-shadow: 0 14px 30px var(--shadow);
    overflow: hidden;
  }
  .floral {
    position: absolute;
    border-radius: 50%;
  }

  /* Front */
  .card-front .floral {
    top: -20px;
    right: 40px;
    width: 250px;
    height: 210px;
    background:
      radial-gradient(circle at 45% 45%, var(--petal-pink) 0 22%, transparent 42%),
      radial-gradient(circle at 65% 62%, var(--petal-coral) 0 14%, transparent 34%),
      radial-gradient(circle at 30% 70%, var(--leaf-green) 0 12%, transparent 32%),
      radial-gradient(ellipse at 55% 55%, var(--leaf-teal) 0 30%, transparent 70%);
  }
  .wordmark {
    position: absolute;
    left: 60px;
    bottom: 62px;
    text-align: center;
  }
  .wordmark-name {
    font-size: 36px;
    font-weight: 700;
    letter-spacing: 1px;
    line-height: 1;
  }
  .wordmark-sub {
    margin-top: 12px;
    font-size: 14px;
    font-weight: 700;
    letter-spacing: 16px;
    padding-left: 16px;
  }

  /* Back */
  .card-back .floral {
    top: 22px;
    left: 50%;
    transform: translateX(-50%);
    width: 230px;
    height: 100px;
    background:
      radial-gradient(circle at 45% 50%, #f8e2b8 0 14%, transparent 30%),
      radial-gradient(circle at 62% 45%, #f3b9c7 0 12%, transparent 28%),
      radial-gradient(circle at 30% 60%, var(--petal-pink) 0 8%, transparent 22%),
      radial-gradient(ellipse at 50% 55%, var(--leaf-green) 0 25%, transparent 65%),
      radial-gradient(ellipse at 50% 50%, var(--leaf-teal) 0 30%, transparent 72%);
  }
  .contact {
    position: absolute;
    top: 132px;
    left: 0;
    right: 0;
    text-align: center;
  }
  .company {
    font-size: 25px;
    font-weight: 700;
    letter-spacing: 0.5px;
  }
  .person {
    margin-top: 10px;
    font-size: 15px;
    font-weight: 700;
  }
  .phone {
    margin-top: 2px;
    font-size: 12px;
  }
  .links {
    margin-top: 10px;
    display: inline-block;
    text-align: left;
    font-size: 12px;
    line-height: 1.55;
  }
  .social {
    display: flex;
    align-items: center;
    gap: 6px;
  }
  .social-mark {
    width: 11px;
    height: 11px;
    background: var(--ink);
    border-radius: 2px;
  }
</style>
</head>
<body>
  <main class="sheet">
    <section class="card card-front">
      <div class="floral" role="img" aria-label="Watercolour bouquet of pink and coral flowers with teal leaves"></div>
      <div class="wordmark">
        <div class="wordmark-name">BRIGHTVOW</div>
        <div class="wordmark-sub">WEDDINGS</div>
      </div>
    </section>

    <section class="card card-back">
      <div class="floral" role="img" aria-label="Watercolour spray of roses and small flowers with teal and green leaves"></div>
      <div class="contact">
        <div class="company">BRIGHTVOW WEDDINGS</div>
        <div class="person">KAY WHITFIELD</div>
        <div class="phone">(480-555-0173)</div>
        <div class="links">
          <div class="web">www.brightvowweddings2go.example</div>
          <div class="social"><span class="social-mark"></span>Brightvow Weddings</div>
          <div class="social"><span class="social-mark"></span>BrightvowWeddings2go</div>
        </div>
      </div>
    </section>
  </main>
</body>
</html>
```